Jackpot Display Wallpaper Design

We develop Jackpot Systems for Casinos and have a web based Jackpot Odometer display. Our software works by superimposing dynamic content over a fixed background.

We require the design of a fixed background of dimensions 1920 x 1080 incorporating higher quality graphical design work and creative ideas.

See File 4 below - "High Hand TEMPLATE". The finished work will resemble this image, with the grey background replaced with your creative design. The black panels will be replaced with your panels, with nice borders and interior shading or pattern. Our software will dynamically superimpose content over the panels. The panels should be of similar size and location to those shown although this is not strictly rigid and you can relocate or resize panels to a limited extent.

The end result when our software runs is something like File 5 below - "High Hand SAMPLE RESULT". Note that the example shows a patterned blue background, a red logo area, and grey shading within the panels.

The text within the panels is rendered dynamically by our application.

** This is a very plain design and only intended to illustrate how we superimpose text and playing cards onto a background. Do not take any design cues from this image.

Please provide the background, and blank panels. The panels can (and should) have some texture or shading that will look good when we render text over them.

Feel free to suggest a font and/or text color that you think would look good against your background and we can render the content in the font / color you suggest.

Target Market(s)

Poker Room facilities and Casinos

Industry/Entity Type

Software

Font styles to use
Sans Serif

Requirements
Must have
• - A graphic design based on the template called High Hand TEMPLATE.
• - 1920 x 1080 Photoshop image using separate layers.
• - The design needs to be edgy and reflect gaming, casinos and poker rooms.
Nice to have
• -Please see files 1, 2, and 3 below by way of "edgy" style guide.
• - For files 1, 2, 3 - ignore the "Bad Beat" wording but focus on the design style by way of example.
• - The background may or may not include the words "Poker" and / or "Jackpot"
• - You can fill in the panels with some sample content to illustrate how it will look.
• - The area at bottom containing scrolling text may be a frame with a border or just an area where we superimpose the scrolling text.

```html
<!DOCTYPE html>
<html lang="en">
<head>
<meta charset="UTF-8">
<title>Jackpot Display Background</title>
<link rel="stylesheet" href="https://fonts.googleapis.com/css2?family=Righteous&family=Montserrat:wght@900&family=Open+Sans:ital,wght@1,400&display=swap">
<style>
  :root {
    --felt-deep: #123f40;
    --felt-mid: #2f6f6c;
    --felt-light: #7fa9a4;
    --chip-red: #8c2a33;
    --panel-black: #151515;
    --panel-edge: #2a2a2a;
    --gold: #f2e600;
    --gold-deep: #c9b800;
    --silver: #cfd3d2;
    --silver-edge: #8d8f8f;
    --marquee-bg: rgba(20, 24, 24, 0.82);
    --marquee-text: #f4f4f4;
  }
  * { box-sizing: border-box; margin: 0; padding: 0; }
  html, body { width: 1200px; height: 675px; overflow: hidden; background: #000; }
  .stage { position: relative; width: 1200px; height: 675px; overflow: hidden; }

  .table-scene {
    position: absolute; inset: 0;
    background:
      radial-gradient(ellipse 320px 140px at 330px 460px, rgba(140,42,51,0.85), transparent 70%),
      radial-gradient(ellipse 300px 200px at 980px 140px, rgba(230,230,230,0.55), transparent 70%),
      radial-gradient(ellipse 260px 220px at 1000px 480px, rgba(200,210,210,0.45), transparent 70%),
      radial-gradient(ellipse 180px 320px at 60px 300px, rgba(240,240,240,0.45), transparent 70%),
      linear-gradient(135deg, var(--felt-mid), var(--felt-deep) 55%, var(--felt-mid));
  }

  .brand-box {
    position: absolute; left: 505px; top: 8px; width: 188px; height: 89px;
    border: 2px solid #111;
    display: flex; justify-content: center; padding-top: 12px;
  }
  .brand-name {
    font-family: "Righteous", sans-serif; font-size: 36px; color: var(--gold); line-height: 1;
  }

  .tab {
    position: absolute; height: 43px;
    display: flex; align-items: center; justify-content: center;
    font-family: "Righteous", sans-serif; font-size: 26px; letter-spacing: 0.5px;
    background: linear-gradient(#3a3a3a, #1b1b1b);
  }
  .panel {
    position: absolute;
    background: radial-gradient(circle at 50% 40%, #262626, var(--panel-black) 75%);
    box-shadow: 0 4px 14px rgba(0,0,0,0.6);
  }

  .jackpot-tab { left: 337px; top: 131px; width: 523px; border: 2px solid var(--gold-deep); color: var(--gold); }
  .jackpot-panel {
    left: 160px; top: 174px; width: 876px; height: 172px;
    border: 3px solid var(--gold);
    display: flex; align-items: center; justify-content: center;
    overflow: hidden;
  }
  .jackpot-amount {
    font-family: "Righteous", sans-serif; font-size: 122px; letter-spacing: 17px;
    color: var(--gold); line-height: 1; padding-left: 17px;
    transform: scaleY(1.22);
    text-shadow: 0 0 2px var(--gold-deep), 0 3px 0 #8a7e00;
  }

  .bonus-tab { left: 338px; top: 386px; width: 523px; border: 2px solid var(--silver-edge); color: var(--silver); }
  .bonus-panel {
    left: 127px; top: 429px; width: 944px; height: 172px;
    border: 2px solid var(--silver-edge);
  }
  .bonus-window {
    position: absolute; left: 338px; top: 428px; width: 523px; height: 173px;
    border: 2px solid var(--silver-edge);
    display: flex; align-items: center; justify-content: center;
    overflow: hidden;
  }
  .bonus-value {
    font-family: "Montserrat", sans-serif; font-weight: 900; font-size: 104px;
    color: var(--silver); line-height: 1; letter-spacing: 1px;
    transform: scaleY(1.3);
    text-shadow: 0 3px 0 #6f7372;
  }

  .marquee {
    position: absolute; left: 0; top: 627px; width: 1200px; height: 36px;
    background: var(--marquee-bg);
    border-top: 1px solid #555; border-bottom: 1px solid #555;
    display: flex; align-items: center; justify-content: center;
    font-family: "Open Sans", sans-serif; font-style: italic; font-size: 24px;
    color: var(--marquee-text); white-space: nowrap; overflow: hidden;
  }
</style>
</head>
<body>
<main class="stage">
  <div class="table-scene" role="img" aria-label="Blurred poker table photo with chips, scattered playing cards and red dice"></div>

  <header class="brand-box"><span class="brand-name">LOGO</span></header>

  <div class="tab jackpot-tab">JACKPOT</div>
  <section class="panel jackpot-panel"><span class="jackpot-amount">345,158.00</span></section>

  <div class="tab bonus-tab">HIGH HAND BONUS</div>
  <section class="panel bonus-panel"></section>
  <div class="bonus-window"><span class="bonus-value">SAMPLE</span></div>

  <footer class="marquee">SCROLLING MARQUEE MESSAGE&nbsp; - SCROLLING MARQUEE MESSAGE - SCROLLING MARQUEE MESSAGE</footer>
</main>
</body>
</html>
```